Business Card Design

Semi retired Estate Agent opening new small business. I am not chasing or wanting to sell everyday houses.. I quite like land and development sales or special projects
..Will need letterheads design and electronic header for electronic mail.
Would like the wording of "Where Know-How Delivers".Envisage simple design..max 3 colours..have strong belief in red , white and blue colours on white background

Would think that the words "Lyle Brannock" be bigger than the words "Real Estate"
I don't want it too busy as many cards are..also has to be classy..!!!
Bold card with my name and mobile number and "Where Know-How Delivers" on the main side and the details on the reverse.
But I am open to suggestions.!!!!!

Target Market(s)

Possible other real estate agents in Western Australia..semi commercial clients.

Industry/Entity Type

Electronic

Contact Information for Business Card

Lyle Brannock Real Estate

Lyle Brannock
Principal and Licensee
lyle@lylebrannockre-example.com.au
mobile 0427581043
ph/f 08 97216083 14B Wattlebird Pde,Claremont ,WA,6010

Requirements
Must have
• I do like the term Where Know-How Delivers"..The reverse side to have address etc..the face side to have name and m obile number

```html
<!DOCTYPE html>
<html lang="en">
<head>
<meta charset="utf-8">
<title>Lyle Brannock Real Estate – Business Card</title>
<link rel="stylesheet" href="https://fonts.googleapis.com/css2?family=Open+Sans:wght@300;400;500&family=Source+Sans+3:wght@300;400&display=swap">
<style>
  :root {
    --stage: #383838;
    --paper: #ffffff;
    --red: #e02229;
    --red-mid: #b01b20;
    --red-deep: #5e0a0c;
    --ink-light: #ffffff;
  }
  * { margin: 0; padding: 0; box-sizing: border-box; }
  html, body {
    width: 1200px; height: 1000px; overflow: hidden;
    background: var(--stage);
    font-family: "Open Sans", Arial, sans-serif;
  }
  .canvas { position: relative; width: 1200px; height: 1000px; }

  .card {
    position: absolute; left: 232px; width: 738px; height: 402px;
    background: var(--paper); overflow: hidden;
  }
  .card--front { top: 76px; }
  .card--back { top: 507px; }

  /* Front */
  .front__field {
    position: absolute; left: 0; top: 0; width: 100%; height: 354px;
    background: radial-gradient(ellipse 62% 95% at 52% 55%, var(--red) 0%, var(--red-mid) 45%, var(--red-deep) 100%);
  }
  .front__name {
    position: absolute; left: 88px; top: 92px;
    color: var(--ink-light);
    font-family: "Source Sans 3", "Open Sans", sans-serif;
    font-weight: 400; font-size: 64px; line-height: 1;
  }
  .front__trade {
    position: absolute; left: 95px; top: 168px;
    color: var(--ink-light);
    font-family: "Source Sans 3", "Open Sans", sans-serif;
    font-weight: 300; font-size: 34px; line-height: 1;
    letter-spacing: 1.5px;
  }
  .front__tagline {
    position: absolute; right: 8px; top: 363px;
    color: var(--red); font-weight: 400; font-size: 28px; line-height: 1;
    letter-spacing: 2.6px;
  }

  /* Back */
  .back__band {
    position: absolute; left: 0; top: 63px; width: 100%; height: 70px;
    background: linear-gradient(to bottom, var(--red-deep) 0%, var(--red-mid) 45%, var(--red) 100%);
    display: flex; align-items: center; justify-content: center; gap: 22px;
    color: var(--ink-light);
  }
  .back__name { font-size: 27px; letter-spacing: 2.2px; font-weight: 400; }
  .back__role { font-size: 18px; letter-spacing: 1.8px; font-weight: 400; padding-top: 4px; }

  .contacts {
    position: absolute; left: 0; top: 164px; width: 100%;
    list-style: none; color: var(--red);
  }
  .contact {
    display: flex; align-items: center; justify-content: center; gap: 8px;
    font-size: 22px; letter-spacing: 1.6px; line-height: 1; height: 38px;
  }
  .contact--email { letter-spacing: 1px; }
  .contact__icon { width: 26px; height: 26px; flex: none; }
</style>
</head>
<body>
<main class="canvas">

  <section class="card card--front" aria-label="Card front">
    <div class="front__field"></div>
    <h1 class="front__name">Lyle Brannock</h1>
    <p class="front__trade">REAL ESTATE</p>
    <p class="front__tagline">Where Know-How Delivers</p>
  </section>

  <section class="card card--back" aria-label="Card back">
    <div class="back__band">
      <span class="back__name">Lyle Brannock</span>
      <span class="back__role">Principal</span>
    </div>
    <ul class="contacts">
      <li class="contact">
        <svg class="contact__icon" viewBox="0 0 24 24" aria-hidden="true">
          <path fill="var(--red)" d="M6.6 2.5c.6-.3 1.3-.1 1.6.5l1.6 3c.3.6.1 1.2-.4 1.6L8 8.6c.7 2.6 2.4 5 4.6 6.6l1.1-1c.5-.4 1.2-.4 1.7 0l2.7 2.1c.5.4.6 1.1.2 1.7l-1.4 2c-.5.7-1.4 1-2.2.7C9 18.8 5.3 13.9 4.7 7.9c-.1-.9.4-1.7 1.2-2.1z"/>
        </svg>
        <span>0427 581 043</span>
      </li>
      <li class="contact">
        <svg class="contact__icon" viewBox="0 0 24 24" aria-hidden="true">
          <g fill="none" stroke="var(--red)" stroke-width="1.4">
            <rect x="6" y="2" width="12" height="8"/>
            <line x1="8" y1="5" x2="16" y2="5"/><line x1="8" y1="7.5" x2="16" y2="7.5"/>
            <rect x="2" y="10" width="20" height="11" rx="1"/>
            <path d="M7 17c1.5-3 8.5-3 10 0"/>
          </g>
        </svg>
        <span>08 9721 6083</span>
      </li>
      <li class="contact contact--email">
        <svg class="contact__icon" viewBox="0 0 24 24" aria-hidden="true">
          <g fill="none" stroke="var(--red)" stroke-width="1.3">
            <rect x="1.5" y="5" width="21" height="15"/>
            <path d="M1.5 5l10.5 9 10.5-9M1.5 20l8-7.5M22.5 20l-8-7.5"/>
          </g>
        </svg>
        <span>lyle@lylebrannockre-example.com.au</span>
      </li>
      <li class="contact">
        <svg class="contact__icon" viewBox="0 0 24 24" aria-hidden="true">
          <path fill="var(--red)" d="M12 1.5a6.5 6.5 0 0 0-6.5 6.5c0 4.8 6.5 14.5 6.5 14.5S18.5 12.8 18.5 8A6.5 6.5 0 0 0 12 1.5zm0 9.2a2.7 2.7 0 1 1 0-5.4 2.7 2.7 0 0 1 0 5.4z"/>
        </svg>
        <span>14B Wattlebird Pde, Ambervale, KR, 6999.</span>
      </li>
    </ul>
  </section>

</main>
</body>
</html>
```